Vorple, an electronic music website !

Hi there,
We are an events agenda (festivals & parties...) specialized in all kinds of electronic music.
It's a big database where peoples come to search there next party and post comments, photos and carpoolings.
Users are between 16 and 45 years old for most of them but the majority is between 18 and 35.
They all love techno music and partying,
We are looking for a design for 2 similar pages.
PSD Uncoded design only for "homepage" and "event page".
Something cool & young but serious and clear.
Thanks

Industry/Entity Type

Events

Number of Pages Required

2 page

Font styles to use
Sans Serif

Requirements
Must have
• Homepage
• - Logo + Name (Black and White logo)
• - Banner (1428x528px in 96ppp or proportional smaller dimension)
• - Slogan "electronic events database" (find police)
• - Principal menu with : « Events », « Map », « Carpooling », « Photos » and « Infos/Contact »
• and
• - Research table (most important) with :
• « Event name », « Kind of music », « Number of people », « Date », « Continent », « Country » and an « advanced search » link.
• - A connexion zone for accounts (Sign In) and a « create account » link.
• - Some social media direct links (Chatterbox, Plimsoll+ and Quibbly)
• - A "focus" zone to present a special event once a month with :
• « Name », « picture (flyer) », « location », « country », « date », « kind of music », the ViewDrum video, and a "more infos" link.
• - An "incoming" zone, with an events list (next ones, 6 or 8) :
• one line per event and, on each line :
• « Name », « picture (flyer) », « location », « country (flag) », « date » and a "more infos" link.
• - A "carpooling" zone, with the list of next carpooling (3 or 4) with on each line :
• « Event name », « picture (flyer) », « country », « date », « seats » and a « more info » link.
• - A map link picture.
• - A calendar (small and easy to understand)
• - A link to photos (only the lasts albums).
• We need a new design for this page, I put a picture of an old design I did by myself (with Paint) just to have an idea. We just want exactly the same things there is on the picture but you can move and change all elements and colors.
• This page is too long for me.
• Page 2 (Event page) : with the document « New » and « Old event page »
• Second most important page
• A lot of things on this page :
• and
• - Event name
• - Flyer (960x960px in 96ppp or proportional dimension)
• - Links to « official website », « tickets » and « add a carpooling »
• - Event informations :
• Location (Continent, Country, Adress)
• Date (from… to…)
• Kind of music
• Number of people
• Price (regular)
• Camping (yes or no)
• - Video ViewDrum
• - Description (long text with lineup and others informations)
• - Carpoolings availables (+ an other link to add a new one)
• - Photos (+ a link to add some)
• - Others similar events (few names)
• - A « Comments » zone where users can whrite what they think about the event.
• Same thing, I made an exemple for this page, please make a new design.
• (Sorry, the website on the document is in French)
• Thanks ;)

```html
<!DOCTYPE html>
<html lang="en">
<head>
<meta charset="utf-8">
<title>Vorple – Electronic Events Database</title>
<link rel="stylesheet" href="https://fonts.googleapis.com/css2?family=Poiret+One&family=Roboto:wght@300;400;500;700&family=Roboto+Condensed:wght@700&display=swap">
<style>
  :root {
    --teal: #2aa79b;
    --teal-bright: #3fd6c6;
    --teal-dark: #0e3d3a;
    --ink: #062220;
    --black: #000000;
    --white: #ffffff;
    --field-hint: #a9b4b3;
    --chatter-blue: #3b5a9a;
  }
  * { box-sizing: border-box; margin: 0; padding: 0; }
  html, body { width: 712px; height: 1200px; overflow: hidden; background: var(--white); }
  body { font-family: "Roboto", Arial, sans-serif; }
  .page { position: relative; width: 712px; height: 1200px; overflow: hidden; }

  /* Hero */
  .hero {
    position: absolute; left: 0; top: 0; width: 712px; height: 400px;
    background: radial-gradient(ellipse at 50% 85%, #2fb8aa 0%, #12564f 40%, #031715 75%, #000 100%);
  }
  .brand {
    position: absolute; left: 0; top: 296px; width: 712px; text-align: center;
    font-family: "Poiret One", sans-serif; font-size: 34px; color: var(--teal-bright);
    letter-spacing: 2px; display: flex; justify-content: center; align-items: center; gap: 12px;
  }
  .brand-mark { width: 22px; height: 22px; background: var(--teal-bright); }

  /* Navigation */
  .main-nav {
    position: absolute; left: 0; top: 400px; width: 712px; height: 44px;
    background: var(--teal); display: flex; align-items: center;
  }
  .main-nav a {
    position: absolute; font-family: "Roboto Condensed", sans-serif; font-weight: 700;
    font-size: 17px; color: var(--ink); text-decoration: none;
  }
  .main-nav a.active { color: var(--white); }

  /* Banner */
  .banner {
    position: absolute; left: 0; top: 444px; width: 712px; height: 356px;
    background: linear-gradient(180deg, #0a1f1e 0%, #050b0b 45%, #000 100%);
  }
  .tagline {
    position: absolute; left: 0; top: 18px; width: 712px; text-align: center;
    font-family: "Roboto", sans-serif; font-weight: 400; font-size: 22px; letter-spacing: 4px; color: var(--white);
  }
  .tagline .dim { color: transparent; -webkit-text-stroke: 0.8px #4a5a5a; }
  .event-title {
    position: absolute; left: 0; top: 32px; width: 712px; text-align: center;
    font-family: "Poiret One", sans-serif; font-size: 290px; line-height: 1; color: var(--white);
    letter-spacing: -4px;
  }
  .event-subtitle {
    position: absolute; left: 26px; top: 300px; width: 660px;
    font-family: "Poiret One", sans-serif; font-size: 40px; color: var(--teal-bright);
    display: flex; justify-content: space-between;
  }

  /* Language strip */
  .lang-strip { position: absolute; left: 0; top: 800px; width: 712px; height: 40px; background: var(--teal); }
  .lang-select {
    position: absolute; left: 554px; top: 12px; width: 72px; height: 17px; background: var(--white);
    font-size: 10px; color: var(--teal); display: flex; align-items: center; gap: 3px; padding-left: 4px;
  }
  .lang-flag { width: 11px; height: 7px; background: linear-gradient(90deg,#2a3f8f 0 40%,#c8202f 40% 60%,#2a3f8f 60%); }
  .lang-arrow { width: 10px; height: 10px; background: var(--black); margin-left: 2px; }

  /* Search panel */
  .search-panel {
    position: absolute; left: 28px; top: 870px; width: 470px; height: 229px;
    background: var(--teal); border-radius: 3px;
  }
  .search-title { position: absolute; left: 20px; top: 10px; font-size: 24px; font-weight: 500; color: var(--white); }
  .field {
    position: absolute; height: 27px; background: var(--white);
    font-size: 16px; color: var(--field-hint); padding: 4px 5px; font-weight: 300;
  }
  .search-btn {
    position: absolute; left: 325px; top: 47px; width: 71px; height: 21px; background: var(--black);
    color: var(--teal-bright); font-size: 13px; text-align: center; line-height: 21px; border-radius: 2px;
  }
  .clear-filter { position: absolute; left: 400px; top: 51px; font-size: 11px; color: var(--white); text-decoration: underline; }
  .divider { position: absolute; left: 236px; top: 104px; width: 1px; height: 100px; background: var(--white); }
  .checkbox { position: absolute; left: 250px; top: 196px; width: 20px; height: 14px; background: var(--white); }

  /* Account */
  .create-account {
    position: absolute; left: 512px; top: 870px; width: 172px; height: 36px; background: var(--teal);
    border-radius: 3px; font-size: 15px; color: var(--ink); text-align: center; line-height: 36px;
  }
  .create-account b { color: var(--white); font-weight: 400; }
  .sign-in {
    position: absolute; left: 515px; top: 928px; width: 169px; height: 171px; background: var(--teal);
    border-radius: 3px; text-align: center;
  }
  .sign-in .member { position: absolute; top: 8px; width: 100%; font-size: 8px; color: var(--ink); }
  .sign-in h2 { position: absolute; top: 16px; width: 100%; font-size: 24px; font-weight: 400; color: var(--white); }
  .sign-in .input {
    position: absolute; left: 20px; width: 128px; height: 20px; background: var(--white);
    font-size: 10px; color: var(--field-hint); text-align: left; padding: 4px; font-style: italic;
  }
  .connect-btn {
    position: absolute; left: 20px; top: 101px; width: 128px; height: 19px; background: var(--black);
    color: var(--teal-bright); font-size: 10px; line-height: 19px;
  }
  .chatter-btn {
    position: absolute; left: 20px; top: 125px; width: 128px; height: 26px; background: var(--chatter-blue);
    color: var(--white); font-size: 10px; display: flex; align-items: center; gap: 6px; padding-left: 6px; border-radius: 2px;
  }
  .chatter-btn span.sq { width: 12px; height: 12px; background: var(--white); }
  .forgot { position: absolute; top: 157px; width: 100%; font-size: 8px; color: var(--ink); text-decoration: underline; font-style: italic; }

  /* Focus band */
  .focus-band { position: absolute; left: 0; top: 1128px; width: 712px; height: 72px; background: var(--black); }
  .focus-title {
    position: absolute; left: 24px; top: 16px; font-family: "Poiret One", sans-serif; font-size: 38px;
    color: var(--white); letter-spacing: 1px;
  }
  .focus-title .accent { color: var(--teal-bright); }
  .focus-wave {
    position: absolute; left: 276px; top: 8px; width: 436px; height: 56px;
    background: radial-gradient(ellipse at 50% 50%, #2aa79b 0%, rgba(42,167,155,0.5) 40%, rgba(0,0,0,0) 75%);
  }
</style>
</head>
<body>
<div class="page">
  <header class="hero" role="img" aria-label="Concert stage with teal laser beams over the crowd">
    <div class="brand"><span class="brand-mark"></span>vorple.events</div>
  </header>

  <nav class="main-nav">
    <a class="active" href="#" style="left:34px">EVENTS</a>
    <a href="#" style="left:167px">MAP</a>
    <a href="#" style="left:274px">CARPOOLING</a>
    <a href="#" style="left:447px">PHOTOS</a>
    <a href="#" style="left:580px">CONTACT US</a>
  </nav>

  <section class="banner" role="img" aria-label="Festival crowd with raised hands in front of stage lights">
    <p class="tagline"><span class="dim">GOOD</span> MUSIC <span class="dim">GOOD</span> VIBES</p>
    <h1 class="event-title">EDM</h1>
    <p class="event-subtitle"><span>F</span><span>E</span><span>S</span><span>T</span><span>I</span><span>V</span><span>A</span><span>L</span><span>&nbsp;</span><span>2</span><span>K</span><span>1</span><span>5</span></p>
  </section>

  <div class="lang-strip">
    <div class="lang-select">English <span class="lang-flag"></span><span class="lang-arrow"></span></div>
  </div>

  <section class="search-panel">
    <h2 class="search-title">Search&gt;&gt;&gt;</h2>
    <div class="field" style="left:20px;top:46px;width:298px;">Event Name</div>
    <div class="search-btn">Search</div>
    <a class="clear-filter" href="#">Clear Filter</a>
    <div class="field" style="left:20px;top:94px;width:200px;">Kind Of Music</div>
    <div class="field" style="left:250px;top:94px;width:200px;">Continent</div>
    <div class="field" style="left:20px;top:142px;width:200px;">Number Of People</div>
    <div class="field" style="left:250px;top:142px;width:200px;">Country</div>
    <div class="field" style="left:20px;top:190px;width:200px;">Date</div>
    <div class="divider"></div>
    <div class="checkbox"></div>
  </section>

  <a class="create-account" href="#">Create <b>New</b> Account</a>

  <section class="sign-in">
    <p class="member">Already a Member ?</p>
    <h2>SIGN IN</h2>
    <div class="input" style="top:54px">username/e-mail id</div>
    <div class="input" style="top:78px">password</div>
    <div class="connect-btn">CONNECT</div>
    <div class="chatter-btn"><span class="sq"></span>Connect with Chatterbox</div>
    <a class="forgot" href="#">forgot password ?</a>
  </section>

  <section class="focus-band">
    <h2 class="focus-title">EDM'S <span class="accent">FOCUS</span></h2>
    <div class="focus-wave" role="img" aria-label="Teal audio waveform decoration"></div>
  </section>
</div>
</body>
</html>
```